I need a business card for myself, being a proprietor of a funeral parlor based in Manila. I'd like the card to have either of the following:
White Font on Black Background
or
Black Font on White Background
No logo is needed however I will appreciate any efforts to show a symbol of eternal happiness, aptly designed with above mentioned colors in mind.
Company name, address and contact on the lower right corner.
Logo or symbol anywhere.
Quillstone Funeral Services
+639174826351
darvik4521@pelmora.com
corner of Brisco Avenue and Velhurst Street
Makati City, Philippines
Thank you.
Update: Please include a small dove in your design. You are free to choose where you would like it on the card.

```html
<!DOCTYPE html>
<html lang="en">
<head>
<meta charset="utf-8">
<title>Quillstone Funeral Services – Business Card</title>
<link href="https://fonts.googleapis.com/css2?family=Merriweather:wght@900&family=Open+Sans:wght@700&display=swap" rel="stylesheet">
<style>
  :root {
    --backdrop-dark: #3f4a45;
    --backdrop-mid: #66716b;
    --backdrop-light: #a9b1ab;
    --card-white: #ffffff;
    --ink: #111111;
    --frame-black: #0d0d0d;
    --emblem-fill: #e6e6e6;
    --emblem-edge: #8a8a8a;
  }
  html, body {
    margin: 0;
    padding: 0;
    overflow: hidden;
  }
  .canvas {
    position: relative;
    width: 1200px;
    height: 702px;
    overflow: hidden;
  }
  .backdrop-texture {
    position: absolute;
    inset: 0;
    background:
      radial-gradient(ellipse at 100% 0%, var(--backdrop-light) 0%, transparent 45%),
      radial-gradient(ellipse at 0% 100%, var(--backdrop-dark) 0%, transparent 55%),
      linear-gradient(135deg, var(--backdrop-dark), var(--backdrop-mid) 55%, var(--backdrop-dark));
  }
  .card-frame {
    position: absolute;
    left: 124px;
    top: 66px;
    width: 954px;
    height: 559px;
    background: var(--frame-black);
  }
  .card-face {
    position: absolute;
    left: 136px;
    top: 78px;
    width: 930px;
    height: 534px;
    background: var(--card-white);
  }
  .card-art {
    position: absolute;
    inset: 0;
  }
  .company-name {
    position: absolute;
    left: 315px;
    top: 142px;
    margin: 0;
    font-family: "Merriweather", Georgia, serif;
    font-weight: 900;
    font-size: 37px;
    line-height: 1;
    color: var(--ink);
    letter-spacing: 0.3px;
  }
  .contact-block {
    position: absolute;
    right: 212px;
    top: 409px;
    margin: 0;
    text-align: right;
    font-family: "Open Sans", Verdana, sans-serif;
    font-weight: 700;
    font-size: 20px;
    line-height: 37.5px;
    color: var(--ink);
  }
  .contact-block span {
    display: block;
  }
</style>
</head>
<body>
  <main class="canvas">
    <div class="backdrop-texture" role="img" aria-label="Dark grey-green distressed grunge texture behind the card"></div>
    <div class="card-frame"></div>
    <div class="card-face"></div>

    <svg class="card-art" width="1200" height="702" viewBox="0 0 1200 702" aria-hidden="true">
      <circle class="emblem" cx="238" cy="175" r="44" fill="var(--emblem-fill)" stroke="var(--emblem-edge)" stroke-width="1.5"/>
      <rect class="rule-top" x="307" y="127" width="653" height="5" fill="var(--ink)"/>
      <rect class="rule-bottom" x="307" y="205" width="653" height="5" fill="var(--ink)"/>
    </svg>

    <h1 class="company-name">Quillstone Funeral Services</h1>

    <address class="contact-block">
      <span class="phone">+639174826351</span>
      <span class="email">darvik4521@pelmora.com</span>
      <span class="street">corner of Brisco Avenue and Velhurst Street</span>
      <span class="city">Makati City, Philippines</span>
    </address>
  </main>
</body>
</html>
```